promotional flyer for Brevara Gym

we are after a double sided a5 leaflet to promote our gym, this is to go out to the general public to entice them into getting membership.

gym membership is £30 per month

it should also include the offer of - if you present this leaflet then there will be no joining fee

some of the features of the gym include

strength machines
cardio machines
functional area
sprung floor mat area

Target Market(s)

Adults 16+ who want to go to the gym and workout

Industry/Entity Type

Gym

Font styles to use
Other font styles liked:
• montserrat Regular

Requirements
Must have
• Clean on brand design
• use images supplied by us
Nice to have
• focus on an inclusive experience as the gym will be advertised to everyone
• should also use our "fitter, stronger, Healthier"

```html
<!DOCTYPE html>
<html lang="en">
<head>
<meta charset="utf-8">
<title>Brevara Gym – A5 Leaflet</title>
<link rel="stylesheet" href="https://fonts.googleapis.com/css2?family=Montserrat:wght@400;600;700&family=Libre+Baskerville:wght@400;700&family=Open+Sans:wght@400&family=Martel:wght@400&family=Passion+One:wght@700&display=swap">
<style>
  :root {
    --backdrop: #ededed;
    --ink-dark: #141414;
    --ink-mid: #232323;
    --orange: #f0652a;
    --orange-deep: #e8531f;
    --white: #ffffff;
    --steel: #c9c9c9;
    --photo-warm: #6b4a32;
    --photo-cool: #3c4660;
    --photo-violet: #6a3d7c;
  }
  * { box-sizing: border-box; margin: 0; padding: 0; }
  html, body { width: 1200px; height: 800px; overflow: hidden; background: var(--backdrop); }
  .sheet-row {
    position: absolute; left: 24px; top: 140px;
    display: flex; gap: 24px;
  }
  .page {
    position: relative; width: 368px; height: 520px; overflow: hidden;
    background: linear-gradient(180deg, var(--ink-mid), var(--ink-dark));
    color: var(--white);
  }

  /* ---------- back: features ---------- */
  .features-photo {
    position: absolute; left: 0; top: 0; width: 368px; height: 180px;
    background: linear-gradient(160deg, var(--photo-cool) 0%, #5a4a48 45%, var(--photo-warm) 100%);
  }
  .features-band {
    position: absolute; left: 0; top: 180px; width: 100%; height: 38px;
    border-top: 2px solid var(--orange); border-bottom: 2px solid var(--orange);
    display: flex; align-items: center; padding-left: 4px;
    font-family: "Libre Baskerville", serif; font-weight: 700; font-size: 14px;
  }
  .features-list {
    position: absolute; left: 40px; top: 236px; list-style: none;
    font-family: "Libre Baskerville", serif; font-size: 9px; line-height: 11px;
  }
  .features-list li::before { content: "•"; color: var(--orange); margin: 0 9px 0 -13px; }
  .offer-box {
    position: absolute; left: 27px; top: 302px; width: 94px; height: 68px;
    border: 2px dashed var(--orange);
    display: flex; align-items: center; justify-content: center; text-align: center;
    font-family: "Libre Baskerville", serif; font-weight: 700; font-size: 7px; line-height: 11.5px;
    text-transform: uppercase;
  }
  .cta {
    position: absolute; left: 16px; top: 394px;
    font-family: "Open Sans", sans-serif; font-size: 18px; line-height: 22px; text-transform: uppercase;
  }

  /* ---------- front ---------- */
  .collage { position: absolute; inset: 0; }
  .price-badge {
    position: absolute; width: 100px; height: 100px; border-radius: 50%;
    background: var(--orange-deep);
    display: flex; align-items: center; justify-content: center; text-align: center;
    font-family: "Montserrat", sans-serif; font-weight: 700; font-size: 17px; line-height: 19px;
  }
  .price-badge::after {
    content: ""; position: absolute; inset: 6px; border-radius: 50%;
    border: 2px dashed var(--white);
  }
  .front .price-badge { left: 17px; top: 224px; }
  .brand-mark {
    position: absolute; left: 50%; transform: translateX(-50%);
    border-radius: 50%; border: 3px solid var(--white);
  }
  .front .brand-mark { top: 304px; width: 68px; height: 68px; }
  .brand-name {
    position: absolute; width: 100%; text-align: center;
    font-family: "Montserrat", sans-serif; font-weight: 400; letter-spacing: 1px; text-transform: uppercase;
  }
  .front .brand-name { top: 378px; font-size: 29px; }
  .tagline {
    position: absolute; width: 100%; text-align: center;
    font-family: "Montserrat", sans-serif; font-weight: 600; color: var(--orange); text-transform: uppercase;
  }
  .front .tagline { top: 421px; font-size: 10px; letter-spacing: 2px; }
  .contact-strip {
    position: absolute; left: 12px; right: 18px; top: 460px;
    display: grid; grid-template-columns: 1.05fr 1.2fr 0.8fr;
    font-family: "Martel", serif; font-size: 8px; line-height: 10px;
  }
  .contact-strip > div { padding: 0 6px; }
  .contact-strip .address { border-right: 2px solid var(--white); padding-left: 0; }
  .contact-strip .online { border-right: 2px solid var(--white); text-align: center; padding-top: 6px; }
  .contact-strip .hours { text-align: right; padding-right: 0; }

  /* ---------- alternate front ---------- */
  .alt-photo {
    position: absolute; left: 0; top: 0; width: 368px; height: 300px;
    background: linear-gradient(170deg, var(--photo-cool) 0%, #4b3f5e 55%, var(--ink-mid) 100%);
  }
  .alt .price-badge { left: 176px; top: 136px; width: 104px; height: 104px; }
  .motto {
    position: absolute; top: 318px; width: 100%; text-align: center;
    font-family: "Passion One", sans-serif; font-weight: 700; font-size: 31px; line-height: 33px;
    color: var(--steel); text-transform: uppercase; letter-spacing: 1px;
  }
  .alt .brand-mark { top: 428px; width: 34px; height: 34px; border-width: 2px; }
  .alt .brand-name { top: 466px; font-size: 14px; }
  .alt .tagline { top: 486px; font-size: 5px; letter-spacing: 1px; }
</style>
</head>
<body>
<main class="sheet-row">

  <section class="page back">
    <div class="features-photo" role="img" aria-label="Photo of strength machines on the gym floor"></div>
    <h2 class="features-band">FEATURES OF THE GYM</h2>
    <ul class="features-list">
      <li>Strength machines</li>
      <li>Cardio machines</li>
      <li>Functional area</li>
      <li>Sprung floor mat area</li>
    </ul>
    <p class="offer-box">If you present<br>this leaflet then<br>there will be no<br>joining fee</p>
    <p class="cta">Start your<br>training today</p>
  </section>

  <section class="page front">
    <svg class="collage" viewBox="0 0 368 520" width="368" height="520">
      <defs>
        <linearGradient id="floor" x1="0" y1="0" x2="1" y2="1">
          <stop offset="0" stop-color="#4a3f52"/><stop offset="1" stop-color="#6b4a32"/>
        </linearGradient>
        <linearGradient id="cycle" x1="0" y1="0" x2="0" y2="1">
          <stop offset="0" stop-color="#48507a"/><stop offset="1" stop-color="#5a4a46"/>
        </linearGradient>
        <linearGradient id="seated" x1="0" y1="0" x2="1" y2="1">
          <stop offset="0" stop-color="#3c4660"/><stop offset="1" stop-color="#7a5a40"/>
        </linearGradient>
        <linearGradient id="press" x1="0" y1="0" x2="0" y2="1">
          <stop offset="0" stop-color="#6a3d7c"/><stop offset="1" stop-color="#3a3036"/>
        </linearGradient>
      </defs>
      <g role="img" aria-label="Photo collage of members training on machines, bikes and weights">
        <polygon points="20,0 300,0 210,95 120,40 70,78 0,20 0,0" fill="url(#floor)"/>
        <polygon points="120,40 262,175 148,300 0,165 0,150" fill="url(#cycle)"/>
        <polygon points="310,0 368,0 368,250 262,175 230,155 210,95" fill="url(#seated)"/>
        <polygon points="262,180 368,200 368,340 320,390 215,290" fill="url(#press)"/>
      </g>
      <line x1="0" y1="14" x2="78" y2="80" stroke="var(--orange)" stroke-width="6"/>
      <line x1="196" y1="110" x2="304" y2="2" stroke="var(--white)" stroke-width="5"/>
      <line x1="118" y1="322" x2="268" y2="180" stroke="var(--orange)" stroke-width="5"/>
    </svg>
    <div class="price-badge">£30 PER<br>MONTH</div>
    <span class="brand-mark" aria-hidden="true"></span>
    <h1 class="brand-name">Brevara Gym</h1>
    <p class="tagline">Fitter | Stronger | Healthier</p>
    <footer class="contact-strip">
      <div class="address">Address - Brevara Gym,<br>Unit 4 Harbour Row,<br>Kestrel Lane, Wendleham,<br>West Sussex, BN99 4QT</div>
      <div class="online">www.brevaragym.co.uk<br>enquiries@brevaragym.co.uk<br>Tel 01632 960418</div>
      <div class="hours">Opening hours<br>mon to Fri<br>6am - 10pm<br>Sat and Sun<br>7am to 7pm</div>
    </footer>
  </section>

  <section class="page alt">
    <div class="alt-photo" role="img" aria-label="Photo of a member using a leg machine"></div>
    <div class="price-badge">£30 PER<br>MONTH</div>
    <p class="motto">Fitter<br>Stronger<br>Healthier</p>
    <span class="brand-mark" aria-hidden="true"></span>
    <h2 class="brand-name">Brevara Gym</h2>
    <p class="tagline">Fitter | Stronger | Healthier</p>
  </section>

</main>
</body>
</html>
```